PPT Template for a company that develops software and intellectual property for use by accountants a

We are a boutique firm that develops specialised reporting applications, financial and non-financial reporting content, checklists and other intellectual property for use by business consultants and accounting firms in particular. The applications and content we are creating is strategically focussed and we are required to produce reports and presentations and our current templates are simply not sufficient.

Excel worksheets, graphs and other graphics are regularly embedded into the presentations
We have our logo in 4 colour palettes and will require the winning version to be provided in all 4 colours plus B&W. There is one single logo but the name “Lantern Trade Pathfinders” is presented in 3 different styles for use depending on the space available etc.
Our clients will typically take our products and rebrand/co brand these (we require them to at least say that there product is “powered by Lantern Trade Pathfinders” with the logo.
The templates you provide will be used to create marketing presentations, proposal presentations and our standard documents that clients will rebrand or cobrand under license.

A Powerpoint Document Slide Template

Cover page layout, back page, intermediate page heading, in colours and styles based on the logo, title styles, and an intermediate or chapter heading slide style. Many of our presentations contain slides with tables, diagrams, flowcharts and text, including simple lists of bullet points. As above, you will see in our style guide that we have four coloured logos – we would like one version in each. We recommend that we finalise the design using the maroon version and then this be used as the base for the other colour palettes.
Again, the cover should be bold and draw attention but remain professional.

We are looking for something that works in both 4:3 and 16:9 (or two templates please)

We like a clear professional and simple look.

Deliverable: PowerPoint template file (.potx extension) for PowerPoint 2007 with at least a “cover” layout, a “title and content” layout, and a simplified slide layout, as well as “back cover”. Please embed any fonts used.

Industry/Entity Type

Financial

```html
<!DOCTYPE html>
<html lang="en">
<head>
<meta charset="utf-8">
<title>Lantern Trade Pathfinders – Slide Template</title>
<link href="https://fonts.googleapis.com/css2?family=Roboto:ital,wght@0,300;0,400;0,500;0,700;1,400&display=swap" rel="stylesheet">
<style>
:root{
  --maroon:#b01c22;
  --maroon-dark:#941419;
  --charcoal:#3a3a3c;
  --grey:#8a8a8c;
  --grey-light:#d9d9d9;
  --stage:#cfd0d2;
  --paper:#ffffff;
  --text:#555;
}
*{box-sizing:border-box;margin:0;padding:0}
html,body{width:1200px;height:896px;overflow:hidden;background:var(--stage);font-family:'Roboto',Arial,sans-serif}
.canvas{position:relative;width:1200px;height:896px}
.slide{position:absolute;width:357px;height:275px;background:var(--paper);overflow:hidden}
.abs{position:absolute}
.footer-band{position:absolute;left:0;right:0;bottom:0;height:6px;background:var(--maroon)}
.footer-band::before{content:"";position:absolute;left:0;right:0;top:-2px;height:1px;background:#999}
.page-no{position:absolute;right:4px;bottom:0;font-size:4px;color:#fff;line-height:6px}
.brand-mini{position:absolute;left:8px;bottom:12px;display:flex;align-items:center;gap:3px}
.brand-mini .dot{width:9px;height:9px;border-radius:50%;background:var(--maroon)}
.brand-mini span{font-size:5px;font-weight:500;color:var(--maroon);line-height:1.1}
.slide-title{position:absolute;left:14px;top:13px;right:12px;font-weight:300;font-size:13px;color:var(--maroon);border-bottom:1px solid var(--grey-light);padding-bottom:2px;letter-spacing:.2px}
.tiny{font-size:4.6px;line-height:1.55;color:var(--text);text-align:justify}
.photo{position:absolute;background:linear-gradient(135deg,#e6e6e6,#9a9a9a)}
.cover-block{left:5px;top:5px;width:347px;height:160px;background:linear-gradient(120deg,var(--maroon) 40%,var(--maroon-dark))}
.cover-rule{left:5px;top:167px;width:347px;height:2px;background:var(--charcoal)}
.cover-title{right:23px;top:76px;text-align:right;color:#fff;font-weight:300;font-size:15.5px;line-height:1.2}
.cover-date{right:23px;top:116px;color:#fff;font-size:7.5px;font-weight:300}
.brand{display:flex;align-items:center;gap:7px}
.brand .dot{width:26px;height:26px;border-radius:50%;background:var(--maroon)}
.brand span{font-size:10px;font-weight:500;color:var(--maroon);line-height:1.1}
.svc-icon{position:absolute;width:44px;height:44px;border-radius:50%;display:flex;align-items:center;justify-content:center}
.svc-title{position:absolute;width:96px;text-align:center;font-size:8px;font-weight:500;color:var(--maroon)}
.svc-text{position:absolute;width:92px;text-align:center;font-size:4.4px;line-height:1.55;color:#999}
.avatar{position:absolute;width:52px;height:52px;border-radius:50%;border:1px solid var(--maroon);padding:2px}
.avatar div{width:100%;height:100%;border-radius:50%;background:linear-gradient(160deg,#eee,#9c9c9c)}
.member{position:absolute;width:80px;text-align:center}
.member b{display:block;font-weight:400;font-size:5.6px;color:#333}
.member i{display:block;font-size:4.2px;color:#666}
.member-text{position:absolute;width:72px;font-size:4.4px;line-height:2.1;color:#999;text-align:justify}
.red{background:var(--maroon)}
.white{color:#fff}
.image-copy{position:absolute;left:22px;top:97px;width:130px;overflow:hidden}
.image-copy h3{font-weight:400;font-size:5.2px;color:#fff;margin-bottom:6px}
.image-copy p{font-size:4.6px;line-height:1.6;color:#fff;text-align:justify;overflow-wrap:break-word}
.image-copy p + p{margin-top:6px}
.contact{position:absolute;left:23px;display:flex;align-items:center;gap:4px;font-size:5.4px;color:#fff;line-height:1.2}
.contact i{width:7px;height:7px;border-radius:50%;background:#fff;flex:none}
</style>
</head>
<body>
<div class="canvas">

  <section class="slide" style="left:46px;top:20px">
    <div class="abs cover-block"></div>
    <div class="abs cover-rule"></div>
    <div class="abs cover-title">WELCOME<br>TO OUR PRESENTATION</div>
    <div class="abs cover-date">Birmingham, March 25, 2011</div>
    <div class="abs brand" style="right:23px;top:212px"><div class="dot"></div><span>Lantern Trade<br>Pathfinders</span></div>
    <div class="footer-band"></div>
  </section>

  <section class="slide" style="left:414px;top:20px">
    <h2 class="slide-title">ABOUT US</h2>
    <div class="photo" style="left:14px;top:34px;width:331px;height:78px" role="img" aria-label="Black and white photo of a smiling business team"></div>
    <p class="abs" style="left:14px;top:126px;width:104px;font-size:5.4px;line-height:1.75;color:var(--maroon)">LOREM IPSUM DOLOR SIT MET CONSECTUR ADIPSICING ELIT, SED DO EUISMOD TEMPOR INCIDIDUNT UT LABORE ET DELORE MAGNA</p>
    <div class="abs" style="left:131px;top:126px;width:207px">
      <p class="tiny" style="font-size:5.3px;line-height:1.8">Lorem ipsum dolor sit amet, consectetur adipisicing elit, sed do eiusmod tempor incididunt ut labore et dolore magna aliqua. Ut enim ad minim veniam, quis nostrud exercitation ullamco laboris nisi ut aliquip ex ea commodo consequat. Duis aute irure dolor in reprehenderit in voluptate velit esse cillum dolore eu fugiat nulla pariatur.</p>
      <p class="tiny" style="font-size:5.3px;line-height:1.8;margin-top:6px">Lorem ipsum dolor sit amet, consectetur adipisicing elit, sed do eiusmod tempor incididunt ut labore et dolore magna aliqua. Ut enim ad minim veniam, quis nostrud exercitation ullamco laboris nisi ut aliquip ex ea commodo consequat. Duis aute irure dolor in reprehenderit in voluptate velit esse cillum dolore eu</p>
    </div>
    <div class="brand-mini"><div class="dot"></div><span>Lantern Trade<br>Pathfinders</span></div>
    <div class="footer-band"><span class="page-no">1</span></div>
  </section>

  <section class="slide" style="left:789px;top:20px">
    <h2 class="slide-title">ABOUT US</h2>
    <div class="abs" style="left:0;right:0;top:61px;height:63px;background:var(--charcoal)"></div>
    <div class="photo" style="left:16px;top:51px;width:107px;height:83px" role="img" aria-label="Black and white portrait of a businesswoman"></div>
    <p class="abs white" style="left:149px;top:73px;width:197px;font-size:5.6px;font-style:italic;line-height:2.1;text-align:justify">Lorem ipsum dolor sit amet<br>consectetur adipisicing elit, sed do eiusmod tempor incididunt ut labore et dolore magna aliqua. Ut enim ad</p>
    <div class="abs" style="left:149px;top:132px;width:197px">
      <p class="tiny">Lorem ipsum dolor sit amet, consectetur adipisicing elit, sed do eiusmod tempor incididunt ut labore et dolore magna aliqua. Ut enim ad minim veniam, quis nostrud exercitation ullamco laboris nisi ut aliquip ex ea commodo consequat. Duis aute irure dolor in reprehenderit in voluptate velit esse cillum dolore eu fugiat nulla pariatur.</p>
      <p class="tiny" style="margin-top:5px">Lorem ipsum dolor sit amet, consectetur adipisicing elit, sed do eiusmod tempor incididunt ut labore et dolore magna aliqua. Ut enim ad minim veniam, quis nostrud exercitation ullamco laboris nisi ut aliquip ex ea commodo consequat. Duis aute irure dolor in reprehenderit in voluptate velit esse cillum dolore eu.</p>
      <p class="tiny" style="margin-top:5px">Fugiat nulla pariatur. Excepteur sint occaecat cupidatat non proident, sunt in culpa qui officia deserunt mollit anim id est laborum. Excepteur sint occaecat cupidatat non proident, sunt in consequat. Duis aute irure dolor in reprehenderit</p>
    </div>
    <div class="brand-mini"><div class="dot"></div><span>Lantern Trade<br>Pathfinders</span></div>
    <div class="footer-band"><span class="page-no">1</span></div>
  </section>

  <section class="slide" style="left:46px;top:308px">
    <h2 class="slide-title">OUR CHART</h2>
    <svg class="abs" style="left:60px;top:45px" width="280" height="160" viewBox="0 0 280 160">
      <g stroke="#555" stroke-width=".8">
        <line x1="11" y1="5" x2="11" y2="131"/><line x1="11" y1="131" x2="270" y2="131"/>
        <line x1="8" y1="5" x2="11" y2="5"/><line x1="8" y1="26" x2="11" y2="26"/><line x1="8" y1="47" x2="11" y2="47"/>
        <line x1="8" y1="68" x2="11" y2="68"/><line x1="8" y1="89" x2="11" y2="89"/><line x1="8" y1="110" x2="11" y2="110"/>
      </g>
      <g>
        <rect x="15" y="41" width="12" height="90" fill="#b01c22"/><rect x="27" y="81" width="12" height="50" fill="#8a8a8c"/><rect x="40" y="90" width="12" height="41" fill="#3a3a3c"/>
        <rect x="67" y="66" width="12" height="65" fill="#b01c22"/><rect x="80" y="41" width="12" height="90" fill="#8a8a8c"/><rect x="93" y="90" width="12" height="41" fill="#3a3a3c"/>
        <rect x="120" y="49" width="12" height="82" fill="#b01c22"/><rect x="133" y="92" width="12" height="39" fill="#8a8a8c"/><rect x="146" y="74" width="12" height="57" fill="#3a3a3c"/>
        <rect x="173" y="53" width="12" height="78" fill="#b01c22"/><rect x="186" y="83" width="12" height="48" fill="#8a8a8c"/><rect x="199" y="44" width="12" height="87" fill="#3a3a3c"/>
      </g>
      <g font-size="8.5" fill="#444" font-family="Roboto, Arial, sans-serif" text-anchor="middle" font-weight="300">
        <text x="34" y="152">2009</text><text x="86" y="152">2010</text><text x="140" y="152">2011</text><text x="193" y="152">2012</text>
      </g>
    </svg>
    <div class="abs" style="left:50px;top:211px;width:80px"><p style="font-size:5px;color:#333"><span style="display:inline-block;width:4px;height:4px;background:var(--maroon);margin-right:2px"></span>LOREM IPSUM</p><p class="tiny" style="font-size:3.6px;line-height:1.4;margin-top:1px">Lorem ipsum dolor sit amet, consectetur adipisicing elit, sed do eiusmod tempor incididunt ut labore et dolore magna</p></div>
    <div class="abs" style="left:149px;top:211px;width:80px"><p style="font-size:5px;color:#333"><span style="display:inline-block;width:4px;height:4px;background:var(--grey);margin-right:2px"></span>LOREM IPSUM</p><p class="tiny" style="font-size:3.6px;line-height:1.4;margin-top:1px">Lorem ipsum dolor sit amet, consectetur adipisicing elit, sed do eiusmod tempor incididunt ut labore et dolore magna</p></div>
    <div class="abs" style="left:245px;top:211px;width:80px"><p style="font-size:5px;color:#333"><span style="display:inline-block;width:4px;height:4px;background:var(--charcoal);margin-right:2px"></span>LOREM IPSUM</p><p class="tiny" style="font-size:3.6px;line-height:1.4;margin-top:1px">Lorem ipsum dolor sit amet, consectetur adipisicing elit, sed do eiusmod tempor incididunt ut labore et dolore magna</p></div>
    <div class="brand-mini"><div class="dot"></div><span>Lantern Trade<br>Pathfinders</span></div>
    <div class="footer-band"><span class="page-no">1</span></div>
  </section>

  <section class="slide" style="left:414px;top:308px">
    <h2 class="slide-title">OUR SERVICES</h2>
    <div class="svc-icon" style="left:45px;top:78px;background:var(--charcoal)">
      <svg width="24" height="24" viewBox="0 0 24 24"><g fill="#fff"><circle cx="12" cy="12" r="7"/><g stroke="#fff" stroke-width="3.2"><line x1="12" y1="2" x2="12" y2="22"/><line x1="2" y1="12" x2="22" y2="12"/><line x1="5" y1="5" x2="19" y2="19"/><line x1="19" y1="5" x2="5" y2="19"/></g></g><circle cx="12" cy="12" r="3" fill="#3a3a3c"/></svg>
    </div>
    <div class="svc-icon" style="left:151px;top:78px;background:var(--maroon)">
      <svg width="24" height="24" viewBox="0 0 24 24"><g fill="#fff"><rect x="4" y="13" width="4" height="8"/><rect x="10" y="10" width="4" height="11"/><rect x="16" y="12" width="4" height="9"/></g><path d="M4 10 L11 5 L15 7" stroke="#fff" stroke-width="2" fill="none"/><path d="M14 4 L19 5 L16 9 Z" fill="#fff"/></svg>
    </div>
    <div class="svc-icon" style="left:266px;top:78px;background:var(--grey)">
      <svg width="24" height="24" viewBox="0 0 24 24" fill="none" stroke="#fff" stroke-width="1.8"><line x1="3" y1="5" x2="21" y2="5"/><rect x="5" y="5" width="14" height="10"/><line x1="12" y1="15" x2="12" y2="18"/><line x1="9" y1="21" x2="12" y2="18"/><line x1="15" y1="21" x2="12" y2="18"/></svg>
    </div>
    <div class="svc-title" style="left:19px;top:135px">OUR SERVICES</div>
    <div class="svc-title" style="left:125px;top:135px">OUR SERVICES</div>
    <div class="svc-title" style="left:240px;top:135px">OUR SERVICES</div>
    <p class="svc-text" style="left:21px;top:147px">dolor sit amet, consectetur adipisicing elit, sed do eiusmod tempor incididunt ut labore et dolore magna aliqua. Ut enim ad minim veniam, quis nostrud exercitation ullamco laboris nisi ut aliquip ex ea cesse cillum dolore eu fugiat nulla pariatur.</p>
    <p class="svc-text" style="left:127px;top:147px">dolor sit amet, consectetur adipisicing elit, sed do eiusmod tempor incididunt ut labore et dolore magna aliqua. Ut enim ad minim veniam, quis nostrud exercitation ullamco laboris nisi ut aliquip ex ea cesse cillum dolore eu fugiat nulla pariatur.</p>
    <p class="svc-text" style="left:242px;top:147px">dolor sit amet, consectetur adipisicing elit, sed do eiusmod tempor incididunt ut labore et dolore magna aliqua. Ut enim ad minim veniam, quis nostrud exercitation ullamco laboris nisi ut aliquip ex ea cesse cillum dolore eu fugiat nulla pariatur.</p>
    <div class="brand-mini"><div class="dot"></div><span>Lantern Trade<br>Pathfinders</span></div>
    <div class="footer-band"><span class="page-no">1</span></div>
  </section>

  <section class="slide" style="left:789px;top:308px">
    <h2 class="slide-title">OUR TEAM</h2>
    <p class="abs" style="left:20px;right:20px;top:53px;text-align:center;font-size:5px;font-style:italic;line-height:2;color:#555">dolor sit amet, consectetur adipisicing elit, sed do eiusmod tempor incididunt ut labore et dolore magna aliqua.<br>Ut enim ad minim veniam, quis nostrud exercitation ullamco laboris nisi ut a</p>
    <div class="avatar" style="left:47px;top:88px"><div role="img" aria-label="Portrait photo of Jonathan Doe"></div></div>
    <div class="avatar" style="left:150px;top:88px"><div role="img" aria-label="Portrait photo of Melanie Doe"></div></div>
    <div class="avatar" style="left:250px;top:88px"><div role="img" aria-label="Portrait photo of Natalie Doe"></div></div>
    <div class="member" style="left:33px;top:149px"><b>JONATHAN DOE</b><i>President</i></div>
    <div class="member" style="left:136px;top:149px"><b>MELANIE DOE</b><i>CEO / Founder</i></div>
    <div class="member" style="left:236px;top:149px"><b>NATALIE DOE</b><i>Vice President</i></div>
    <p class="member-text" style="left:37px;top:172px">dolor sit amet, consectetur adipisicing elit, sed do eiusmod tempor incididunt ut labore et dolore magna aliqua. Ut enim ad minim veniam, quis nostrud exercitation</p>
    <p class="member-text" style="left:140px;top:172px">dolor sit amet, consectetur adipisicing elit, sed do eiusmod tempor incididunt ut labore et dolore magna aliqua. Ut enim ad minim veniam, quis nostrud exercitation</p>
    <p class="member-text" style="left:240px;top:172px">dolor sit amet, consectetur adipisicing elit, sed do eiusmod tempor incididunt ut labore et dolore magna aliqua. Ut enim ad minim veniam, quis nostrud exercitation</p>
    <div class="brand-mini"><div class="dot"></div><span>Lantern Trade<br>Pathfinders</span></div>
    <div class="footer-band"><span class="page-no">1</span></div>
  </section>

  <section class="slide red" style="left:46px;top:598px">
    <h2 class="abs white" style="left:13px;top:17px;font-weight:300;font-size:12.5px">IMAGE TEXT</h2>
    <div class="image-copy">
      <h3>LOREM IPSUM DOLOR SIT MET</h3>
      <p>Lorem ipsum dolor sit amet, consectetur adipisicing elit, sed do eiusmod tempor incididunt ut labore et dolore magna aliqua. Ut enim ad minim veniam, quis nostrud exercitation ullamco laboris nisi ut aliquip ex ea commodo consequat. Duis aute irure dolor in reprehenderit in voluptate velit esse cillum dolore eu fugiat nulla pariatur.</p>
      <p>Lorem ipsum dolor sit amet, consectetur adipisicing elit, sed do eiusmod tempor incididunt ut labore et dolore magna aliqua. Ut enim ad minim veniam, quis nostrud exercitation ullamco laboris nisi ut aliquip ex ea commodo consequat. Duis aute irure dolor in reprehenderit in voluptate velit esse cillum dolore eu.</p>
    </div>
    <div class="photo" style="left:176px;top:0;width:181px;height:275px;background:linear-gradient(160deg,#f2f2f2,#b5b5b5 60%,#6e6e6e)" role="img" aria-label="Black and white photo of a smiling businesswoman and businessman"></div>
    <div class="brand-mini" style="bottom:10px"><div class="dot" style="background:#fff"></div><span style="color:#fff">Lantern Trade<br>Pathfinders</span></div>
  </section>

  <section class="slide red" style="left:414px;top:598px">
    <div class="abs" style="left:156px;top:120px;width:44px;height:44px;border-radius:50%;background:#fff;display:flex;align-items:center;justify-content:center">
      <svg width="20" height="30" viewBox="0 0 20 30"><circle cx="11" cy="5" r="3.5" fill="#b01c22"/><path d="M7 11 H13 L10 25 H14 L13 28 H4 L5 25 L8 14 H6 Z" fill="#b01c22"/></svg>
    </div>
    <div class="abs" style="left:128px;top:174px;width:101px;height:1px;background:#fff"></div>
    <div class="abs white" style="left:0;right:0;top:181px;text-align:center;font-weight:300;font-size:11.5px">SECTION TITLE</div>
  </section>

  <section class="slide" style="left:789px;top:598px">
    <div class="abs brand" style="left:21px;top:42px"><div class="dot"></div><span>Lantern Trade<br>Pathfinders</span></div>
    <div class="abs red" style="left:0;right:0;top:102px;bottom:0;background:linear-gradient(100deg,var(--maroon) 55%,var(--maroon-dark))"></div>
    <div class="abs white" style="left:23px;top:146px;font-weight:300;font-size:12px">THANK YOU</div>
    <div class="abs white" style="left:23px;top:162px;font-size:5.4px">FOR YOUR TIME</div>
    <div class="contact" style="top:195px"><i></i><span>4120 Harbor Crest Road Ste 310<br>Millbrook, Ohio 43017</span></div>
    <div class="contact" style="top:215px"><i></i><span>1.800.555.0142</span></div>
    <div class="contact" style="top:230px"><i></i><span>hello@lanterntrade.example</span></div>
    <div class="contact" style="top:245px"><i></i><span>www.lanterntrade.example</span></div>
  </section>

</div>
</body>
</html>
```